Voltara Solutions Ltd - Project for new electric vehicle charging company

Please use Voltara Solutions Ltd logo & artwork instead of Brightwell.

We would like to produce a leaflet to advertise our electric vehicle charging company to build a reputation and workflow in the local area.

We would like to use the attached logo and maintain the colour palette of the of the logo to be simple, modern and effective.

I have over 15 years experience in the electrical industry and have direct access to the latest technology in electric vehicle charging.

All quotes to remain fixed costs subject to survey of the property and maintenance options can be available.

We can also offer further remedial works to any property through our sister company Brightwell Solutions Ltd.

Target Market(s)

Domestic / commercial customers

Requirements
Must have
• Voltara Solutions Ltd logo and colour palette.
Should not have
• Brightwell logo, Email or website address.

```html
<!DOCTYPE html>
<html lang="en">
<head>
<meta charset="utf-8">
<title>Voltara Solutions Ltd – Leaflet</title>
<link rel="stylesheet" href="https://fonts.googleapis.com/css2?family=Montserrat:wght@400;500;600;700;800&family=Roboto:wght@400&display=swap">
<style>
  :root {
    --stage: #5ee3d4;
    --paper: #ffffff;
    --teal-deep: #069a8a;
    --teal-ring: #3fb9aa;
    --teal-panel: #05b5a2;
    --teal-brand: #12b3a0;
    --teal-icon: #079585;
    --ink: #1f1f1f;
    --grey-text: #6f6f6f;
    --line-teal: #14b3a1;
  }
  * { margin: 0; padding: 0; box-sizing: border-box; }
  html, body { width: 1200px; height: 1200px; overflow: hidden; }
  body {
    background: var(--stage);
    font-family: "Montserrat", Arial, sans-serif;
    position: relative;
  }
  .leaflet {
    position: absolute;
    left: 237px; top: 84px;
    width: 726px; height: 1031px;
    background: var(--paper);
    overflow: hidden;
  }
  .leaflet-shapes { position: absolute; inset: 0; }
  .abs { position: absolute; }

  .hero-title {
    left: 39px; top: 90px;
    color: #fff; font-weight: 800;
    font-size: 41px; line-height: 47px;
    letter-spacing: 0.2px;
  }
  .hero-sub {
    left: 39px; top: 183px;
    color: #fff; font-weight: 500; font-size: 19.6px;
  }
  .hero-copy {
    left: 37px; top: 230px;
    color: #fff; font-weight: 600; font-size: 11.2px; line-height: 17px;
  }

  .brand {
    left: 450px; top: 42px;
    display: flex; align-items: center; gap: 8px;
    color: var(--teal-brand); font-weight: 500;
  }
  .brand-dot { width: 56px; height: 56px; border-radius: 50%; background: var(--teal-brand); }
  .brand-name { font-size: 33px; line-height: 34px; }
  .brand-tag { font-size: 8px; letter-spacing: 5px; margin-top: 2px; }

  .offer-title {
    left: 39px; top: 507px;
    font-weight: 800; font-size: 30px; color: var(--ink);
  }
  .offer-title span { color: var(--teal-brand); }
  .offer-copy {
    left: 36px; top: 575px;
    color: var(--grey-text); font-size: 13.4px; line-height: 19.2px; font-weight: 400;
  }

  .service-title { color: #fff; font-weight: 700; font-size: 18px; line-height: 22px; }
  .service-text { color: #fff; font-weight: 500; font-size: 15.4px; line-height: 21.8px; }

  .contact-bar {
    left: 43px; top: 977px;
    display: flex; align-items: center; gap: 8px;
    font-family: "Roboto", Arial, sans-serif; font-size: 14.2px; color: #222;
  }
  .contact-icon {
    width: 22px; height: 22px; border-radius: 50%; background: var(--teal-icon);
    display: flex; align-items: center; justify-content: center;
  }
  .contact-sep { margin: 0 6px; }
</style>
</head>
<body>
<main class="leaflet">
  <svg class="leaflet-shapes" width="726" height="1031" viewBox="0 0 726 1031">
    <defs>
      <linearGradient id="sceneFade" x1="0" y1="0" x2="0" y2="1">
        <stop offset="0" stop-color="#ffffff"/>
        <stop offset="0.35" stop-color="#ececec"/>
        <stop offset="1" stop-color="#f3f3f3"/>
      </linearGradient>
      <radialGradient id="chargerScene" cx="0.6" cy="0.45" r="0.6">
        <stop offset="0" stop-color="#4d6a3a"/>
        <stop offset="0.55" stop-color="#2f3f2a"/>
        <stop offset="1" stop-color="#232523"/>
      </radialGradient>
      <clipPath id="ringArea">
        <rect x="0" y="0" width="410" height="392"/>
      </clipPath>
    </defs>

    <rect class="backdrop-scene" role="img" aria-label="Faded photo of a house with solar panels and an EV charger" x="0" y="370" width="726" height="661" fill="url(#sceneFade)"/>

    <path d="M400 15 Q 440 90 440 140" fill="none" stroke="var(--line-teal)" stroke-width="1"/>
    <circle cx="400" cy="14" r="8" fill="var(--teal-panel)"/>
    <path d="M0 410 Q 120 490 260 450" fill="none" stroke="var(--line-teal)" stroke-width="1"/>
    <circle cx="28" cy="421" r="12" fill="var(--teal-panel)"/>
    <circle cx="263" cy="428" r="8" fill="var(--teal-panel)"/>

    <circle cx="152" cy="155" r="258" fill="var(--teal-deep)"/>
    <circle cx="524" cy="373" r="268" fill="var(--teal-ring)" clip-path="url(#ringArea)"/>
    <circle class="hero-photo" role="img" aria-label="Photo of a black wallbox charger connected to a white electric car in front of trees" cx="524" cy="373" r="245" fill="url(#chargerScene)"/>

    <line x1="39" y1="217" x2="274" y2="217" stroke="#fff" stroke-width="1.2"/>
    <rect x="139" y="214" width="34" height="6" fill="#fff"/>
    <line x1="37" y1="563" x2="290" y2="563" stroke="var(--line-teal)" stroke-width="1.2"/>
    <rect x="146" y="560" width="36" height="6" fill="var(--line-teal)"/>

    <rect x="37" y="712" width="651" height="239" rx="12" fill="var(--teal-panel)"/>
    <g fill="var(--teal-icon)">
      <circle cx="87" cy="783" r="30"/>
      <circle cx="413" cy="783" r="30"/>
      <circle cx="87" cy="892" r="30"/>
      <circle cx="413" cy="892" r="30"/>
    </g>
    <g fill="none" stroke="#fff" stroke-width="1.3" stroke-linecap="round" stroke-linejoin="round">
      <circle cx="91" cy="774" r="7"/>
      <path d="M92 769 l-3 5 h4 l-3 5"/>
      <path d="M70 793 v-5 l5 -2 l5 -6 h18 l6 6 l4 2 v5 z"/>
      <circle cx="78" cy="793" r="3"/><circle cx="99" cy="793" r="3"/>
      <rect x="402" y="770" width="16" height="27" rx="2"/>
      <rect x="405" y="773" width="10" height="8"/>
      <path d="M411 774 l-3 4 h4 l-3 4"/>
      <path d="M400 797 h20 M418 780 h4 v12 q3 0 3 -4 v-10 M423 774 v4"/>
      <rect x="77" y="878" width="14" height="27" rx="2"/>
      <path d="M79 882 h10 M85 888 l-3 5 h4 l-3 5 M75 905 h18 M91 893 l6 -6 l3 3 M97 887 l3 -3"/>
      <rect x="402" y="880" width="18" height="24" rx="3"/>
      <circle cx="411" cy="890" r="6"/>
      <path d="M412 887 l-2 3 h3 l-2 3 M420 884 q8 0 8 8 v6 q0 4 -4 4"/>
    </g>
  </svg>

  <h1 class="abs hero-title">15 Years<br>Experience</h1>
  <p class="abs hero-sub">in the electrical industry</p>
  <p class="abs hero-copy">Proin ac leo quis odio ullamcorper egestas.<br>Nunc dictum ante eget aliquam aliquet.<br>Donec fermentum imperdiet pulvinar.<br>Donec ac lacinia ligula, et fermentum.</p>

  <div class="abs brand">
    <div class="brand-dot"></div>
    <div>
      <div class="brand-name">Voltara</div>
      <div class="brand-tag">SOLUTIONS LTD</div>
    </div>
  </div>

  <h2 class="abs offer-title">What <span>We Offer</span></h2>
  <p class="abs offer-copy">Nunc aliquet enim eget enim consequat<br>porta. Nullam porta metus sed lacus<br>varius luctus. Fusce blandit urna nec tortor mollis<br>mattis.Aliquam tincidunt elementum vulputate. Nam gravida dui nisl, dapibus posuere mi<br>venenatis et. Phasellus vitae nunc eget eros tempus volutpat.Nam a purus sagittis, hendrerit<br>purus vitae, convallis nisl. Nulla pharetra tincidunt ante, eu interdum lectus vehicula sed.</p>

  <div class="abs service" style="left:126px; top:741px;">
    <h3 class="service-title">Aenean at laoreet tellus</h3>
    <p class="service-text">Phasellus convallis, urna ut<br>rhoncus rhoncus, sem tortor<br>porttitor nulla.</p>
  </div>
  <div class="abs service" style="left:452px; top:741px;">
    <h3 class="service-title">Aenean at laoreet tellus</h3>
    <p class="service-text">Phasellus convallis, urna ut<br>rhoncus rhoncus, sem tortor<br>porttitor nulla.</p>
  </div>
  <div class="abs service" style="left:126px; top:850px;">
    <h3 class="service-title">Aenean at laoreet tellus</h3>
    <p class="service-text">Phasellus convallis, urna ut<br>rhoncus rhoncus, sem tortor<br>porttitor nulla.</p>
  </div>
  <div class="abs service" style="left:452px; top:850px;">
    <h3 class="service-title">Aenean at laoreet tellus</h3>
    <p class="service-text">Phasellus convallis, urna ut<br>rhoncus rhoncus, sem tortor<br>porttitor nulla.</p>
  </div>

  <div class="abs contact-bar">
    <span class="contact-icon"><svg width="12" height="12" viewBox="0 0 24 24"><path d="M6.6 10.8a15 15 0 0 0 6.6 6.6l2.2-2.2a1 1 0 0 1 1-.25 11.4 11.4 0 0 0 3.6.57 1 1 0 0 1 1 1V20a1 1 0 0 1-1 1A17 17 0 0 1 3 4a1 1 0 0 1 1-1h3.5a1 1 0 0 1 1 1c0 1.25.2 2.45.57 3.57a1 1 0 0 1-.25 1z" fill="#fff"/></svg></span>
    <span>0121-555-0184</span><span class="contact-sep">|</span>
    <span class="contact-icon"><svg width="12" height="12" viewBox="0 0 24 24" fill="none" stroke="#fff" stroke-width="2"><rect x="3" y="5" width="18" height="14" rx="2"/><path d="M3 7l9 6 9-6"/></svg></span>
    <span>enquiries@voltara-solutions.com</span><span class="contact-sep">|</span>
    <span class="contact-icon"><svg width="13" height="13" viewBox="0 0 24 24" fill="none" stroke="#fff" stroke-width="1.8"><circle cx="12" cy="12" r="9"/><path d="M3 12h18M12 3c3 3 3 15 0 18M12 3c-3 3-3 15 0 18"/></svg></span>
    <span>www.voltara-solutions.co.uk</span>
  </div>
</main>
</body>
</html>
```